Qb Panes

We need a website design for a company based in Texas that specializes in doors and and windows.
Qb Pane is a leading window manufacturer of aluminum and vinyl windows, both serving the replacement and new construction markets. Qb Pane Inc. was created over 25 years ago when two existing window manufacturers with excellent reputations in their fields - merged. Qb Pane offers a complete line conforming to the needs of residential and commercial window markets.
The final design should be something that communicates professionalism and features they're key value propositions.
Example websites we like:
http://layouts.pebblecraft.example/zx/satchel/
http://layouts.pebblecraft.example/zx/splashyard/
http://layouts.pebblecraft.example/zx/rebuildr2/
This design should format the existing content to be more visually organized, improve the fonts to clearer and more readable, and make it easier for users to find services.
Brand guide is attached
Website images can be found here: https://docs.vaultcrate.example/7kRTmwQzLpXeBd
Target Market(s)
Windows
Number of Pages Required
1 page
Look and feel
Each slider illustrates characteristics of the customer's brand and the style your logo design should communicate.

```html
<!DOCTYPE html>
<html lang="en">
<head>
<meta charset="utf-8">
<title>Qb Pane – Windows &amp; Doors</title>
<link rel="stylesheet" href="https://fonts.googleapis.com/css2?family=Crimson+Text:wght@400;600&family=Open+Sans:wght@400;600;700&display=swap">
<style>
:root{
  --teal:#3a6563;
  --teal-dark:#2e5553;
  --crimson:#a3193a;
  --gold:#c49a2c;
  --ink:#333;
  --muted:#666;
  --pale:#f1f5f7;
  --hero:#edf2f4;
  --admin:#23282d;
  --rule:#d6d6d6;
  --link:#2a7ab8;
  --placeholder:#e3e7ea;
}
*{box-sizing:border-box;margin:0;padding:0}
html,body{width:1200px;height:3502px;overflow:hidden}
body{position:relative;background:#fff;font-family:"Open Sans",Arial,sans-serif;color:var(--ink)}
.abs{position:absolute}
.serif{font-family:"Crimson Text",Georgia,serif}

.admin-bar{left:0;top:0;width:1200px;height:28px;background:var(--admin);color:#ddd;font-size:11px;display:flex;align-items:center;padding:0 14px;gap:22px}
.admin-bar .right{margin-left:auto}

.topbar{left:0;top:28px;width:1200px;height:37px;background:var(--teal-dark);color:#fff;font-family:"Crimson Text",Georgia,serif;font-size:15px;display:flex;align-items:center;justify-content:flex-end;padding-right:40px;gap:26px}
.topbar span{display:flex;align-items:center;gap:6px}
.social{display:flex;gap:8px}
.social i{width:24px;height:24px;border:2px solid #fff;border-radius:50%;display:block}

.header{left:0;top:65px;width:1200px;height:80px;background:#fff;display:flex;align-items:center;padding:0 30px}
.logo{font-family:"Crimson Text",Georgia,serif;font-size:40px;color:var(--crimson);font-weight:400}
.nav{margin-left:auto;display:flex;gap:24px;font-family:"Crimson Text",Georgia,serif;font-size:15px;color:var(--gold);letter-spacing:.5px}

.hero{left:0;top:145px;width:1200px;height:555px;background:var(--hero)}
.hero-photo{left:82px;top:30px;width:502px;height:525px;background:linear-gradient(160deg,#dfe6ea,#9fb6cf 55%,#2c3440)}
.hero-title{left:620px;top:195px;width:460px;text-align:center;font-size:31px;line-height:1.2;color:#333;font-weight:400}
.hero-sub{left:620px;top:312px;width:460px;text-align:center;font-size:18px;letter-spacing:1px;color:#444}
.btn{left:728px;top:404px;width:241px;height:42px;background:var(--crimson);color:#fff;font-size:18px;display:flex;align-items:center;justify-content:center;letter-spacing:.5px}

.label{height:42px;background:var(--crimson);color:#fff;font-family:"Crimson Text",Georgia,serif;font-size:22px;display:flex;align-items:center;justify-content:center;box-shadow:0 4px 0 #e4e4e4}

.works-list{left:124px;top:800px;list-style:none;font-size:14px;line-height:24px;color:var(--link)}
.works-list li{display:flex;align-items:center;gap:18px}
.works-list li::before{content:"";width:16px;height:12px;border:2px solid var(--gold);border-width:2px 0;background:linear-gradient(var(--gold),var(--gold)) center/100% 2px no-repeat}
.intro{left:460px;top:742px;width:614px;font-size:13px;line-height:19.5px;color:var(--muted)}
.more{font-size:18px;color:#444}

.gallery{left:124px;top:953px;display:flex;gap:25px}
.gallery div{width:221px;height:280px;box-shadow:10px 10px 0 #e3e3e3}
.g1{background:linear-gradient(#8aa86a,#6a4a34 60%,#4f7d3a)}
.g2{background:linear-gradient(#f4f1ea,#d9d2c2 60%,#b9b3a5)}
.g3{background:linear-gradient(#eef1f2,#c9d0cf 55%,#8e8a80)}
.g4{background:linear-gradient(#c9cfcd,#9fb28d 55%,#d8dad5)}

.rule{left:124px;width:952px;height:2px;background:var(--rule)}

.news-logo{left:124px;top:1466px;width:285px;height:94px;background:var(--placeholder)}
.card{width:284px;border:1px solid #ddd;padding:12px 16px;font-size:12px;line-height:19px;color:var(--muted)}
.card h3{font-weight:400;font-size:16px;line-height:19px;color:#444;margin-bottom:8px}
.card a{color:var(--link);text-decoration:none;display:block}

.certs{left:0;top:1856px;width:1200px;height:374px;background:var(--pale)}
.badge-a{left:518px;top:1966px;width:66px;height:79px;background:#1c8fcf}
.badge-b{left:612px;top:1989px;width:88px;height:34px;background:#1f5c86;border-radius:3px}
.stats{left:250px;top:2055px;width:700px;height:175px;background:var(--teal);color:#fff;display:flex}
.stat{flex:1;text-align:center;padding-top:56px}
.stat b{display:block;font-size:38px;font-weight:700;line-height:1}
.stat span{display:block;font-size:15px;margin-top:22px}

.service{width:300px;text-align:center}
.service svg{display:block;margin:0 auto}
.service h4{font-family:"Crimson Text",Georgia,serif;font-weight:400;font-size:20px;margin-top:34px;color:#333;letter-spacing:.5px}
.service p{font-size:12.5px;line-height:20px;color:var(--muted);margin-top:6px;padding:0 6px}

.reviews{left:0;top:2716px;width:1200px;height:350px;background:var(--pale)}
.stars{left:0;top:2812px;width:1200px;text-align:center;color:#d39a1d;font-size:20px;letter-spacing:4px}
.quote{left:270px;top:2852px;width:660px;text-align:center;font-size:15px;line-height:22px;color:#333}
.quote em{font-style:normal;color:var(--link)}
.author{left:0;top:2950px;width:1200px;text-align:center;font-size:20px;color:#333}
.author::before{content:"";display:block;width:80px;height:1px;background:#ccc;margin:0 auto 20px}

.footer{left:0;top:3066px;width:1200px;height:390px;background:var(--teal)}
.map{left:124px;top:3140px;width:448px;height:246px;background:linear-gradient(135deg,#e6ecdc,#d7e2ec 50%,#e9e4d6)}
.contact{left:628px;top:3162px;list-style:none;color:#fff;font-family:"Crimson Text",Georgia,serif;font-size:16px}
.contact li{display:flex;align-items:center;gap:14px;height:38px}
.contact svg{width:22px;height:22px;flex:none}

.bottom{left:0;top:3456px;width:1200px;height:46px;background:#222;color:#888;font-size:12px;display:flex;align-items:center;padding:0 124px}
.bottom .icons{margin-left:auto;display:flex;gap:22px}
.bottom .icons i{width:16px;height:16px;background:#666;display:block;border-radius:50%}
</style>
</head>
<body>

<div class="abs admin-bar"><span>Site Admin</span><span>5</span><span>0</span><span>+ New</span><span>Edit Page</span><span>Performance</span><span>Enable Visual Builder</span><span class="right">Howdy, admin</span></div>

<div class="abs topbar">
  <span><svg width="14" height="14" viewBox="0 0 14 14"><path d="M7 1a4 4 0 0 1 4 4c0 3-4 8-4 8S3 8 3 5a4 4 0 0 1 4-4z" fill="#fff"/></svg>FIND A DEALER</span>
  <span><svg width="14" height="14" viewBox="0 0 14 14"><rect x="2" y="1" width="10" height="12" fill="#fff"/></svg>REQUEST A QUOTE</span>
  <span><svg width="14" height="14" viewBox="0 0 14 14"><path d="M3 1l3 3-2 2c1 2 2 3 4 4l2-2 3 3-2 2C6 13 1 8 1 3z" fill="#fff"/></svg>877-555-0142</span>
  <div class="social"><i></i><i></i><i></i><i></i></div>
</div>

<header class="abs header">
  <div class="logo">Qb Pane</div>
  <nav class="nav"><span>HOMES</span><span>ABOUT US</span><span>SERVICES</span><span>GALLERY</span><span>CONTACT</span></nav>
</header>

<section class="abs hero">
  <div class="abs hero-photo" role="img" aria-label="Photo of a smiling homeowner couple"></div>
</section>
<h1 class="abs hero-title serif">Your Logical Choice for Home or Business</h1>
<p class="abs hero-sub serif">A GREAT WINDOW AT GREAT PRICE</p>
<div class="abs btn serif">See offer and prices</div>

<div class="abs label" style="left:124px;top:747px;width:315px">Recent works</div>
<ul class="abs works-list"><li>Sunroom</li><li>Screenroom</li><li>Patio cover</li><li>Arbor</li></ul>
<p class="abs intro">Qb Pane and Door has been proudly serving central Wyoming for 10 years. We are a locally owned and operated business providing excellent window and door installation, maintenance, and service for commercial and residential buildings. Our experienced team can handle your next project, from servicing your existing windows or doors, to designing a unique custom piece. Call us today for a free estimate!</p>
<div class="abs more" style="left:476px;top:874px">View more</div>

<div class="abs gallery">
  <div class="g1" role="img" aria-label="Photo of a patio cover with French doors"></div>
  <div class="g2" role="img" aria-label="Photo of a bright living room with large windows"></div>
  <div class="g3" role="img" aria-label="Photo of a screened patio room"></div>
  <div class="g4" role="img" aria-label="Photo of a sunroom overlooking a field"></div>
</div>

<div class="abs rule" style="top:1315px"></div>

<div class="abs label" style="left:447px;top:1373px;width:306px">Latest news</div>
<div class="abs news-logo" role="img" aria-label="Partner glass brand mark"></div>
<article class="abs card" style="left:458px;top:1466px">
  <h3>Qb Pane Latest To Add Innovative Brightvane® Dynamic Glass To Their Sales Offerings</h3>
  Glazewell, LLC. has announced a sales and distribution partnership with Qb Pane Inc., that will enable the company to offer self-tinting Brightvane® Dynamic Glass with its full line of window, door, and sunroom products.
  <a>read more</a>
</article>
<article class="abs card" style="left:792px;top:1466px">
  <h3>Buy Local from Qb Pane Inc.</h3>
  If buying local is important to you, consider replacement windows from Qb Pane. Based in Dallas/Fort Worth their plant makes over 100,000 windows a year and 100% of the supplies used in making their windows are from the US. Few window companies are as dedicated
  <a>read more</a>
</article>

<div class="abs rule" style="top:1805px"></div>

<section class="abs certs"></section>
<div class="abs label" style="left:447px;top:1896px;width:306px">Certifications &amp; Awards</div>
<div class="abs badge-a" role="img" aria-label="Efficiency partner badge"></div>
<div class="abs badge-b" role="img" aria-label="Accredited business badge"></div>
<div class="abs stats">
  <div class="stat"><b>24 +</b><span>Years Experience</span></div>
  <div class="stat"><b>2000 +</b><span>Works</span></div>
</div>

<div class="abs label" style="left:447px;top:2272px;width:306px">What we do</div>
<div class="abs service" style="left:114px;top:2363px">
  <svg width="84" height="84" viewBox="0 0 84 84" fill="none" stroke="#999" stroke-width="2"><rect x="2" y="2" width="80" height="80"/><rect x="10" y="10" width="64" height="64"/><line x1="42" y1="10" x2="42" y2="74"/><line x1="10" y1="40" x2="74" y2="40"/></svg>
  <h4>RESIDENTIAL</h4>
  <p>Qb Pane specializes in window for residential . If your windows need to be replaced, our teams can tackle the removal and disposal of your old windows.</p>
</div>
<div class="abs service" style="left:450px;top:2363px">
  <svg width="84" height="84" viewBox="0 0 84 84" fill="none" stroke="#999" stroke-width="2"><rect x="6" y="2" width="72" height="80"/><line x1="42" y1="2" x2="42" y2="82"/><path d="M42 8l26-4v76l-26-4z"/></svg>
  <h4>COMMERCIAL</h4>
  <p>In addition to window replacement, our team of highly trained experts are able to install windows of all sizes for commercial properties.</p>
</div>
<div class="abs service" style="left:784px;top:2363px">
  <svg width="84" height="84" viewBox="0 0 84 84" fill="none" stroke="#999" stroke-width="2"><rect x="4" y="4" width="76" height="14"/><rect x="4" y="24" width="76" height="14"/><rect x="4" y="44" width="76" height="14"/><rect x="4" y="64" width="76" height="14"/></svg>
  <h4>VINYL SERIES</h4>
  <p>Qb Pane can assist you with Vinyl series . Keep your home warm in the winter and cool in the summer with energy-efficient windows.</p>
</div>
<div class="abs more" style="left:556px;top:2640px">View more</div>

<section class="abs reviews"></section>
<div class="abs stars">★★★★★</div>
<p class="abs quote">" They were really good. I really liked the workers, they are guys that have been there for years. Very trustworthy guys. They framed out 3 doors with Cedar which was great. They were <em>really great</em> and did a really good job. I can't recommend them enough. "</p>
<div class="abs author">Marissa T</div>

<footer class="abs footer"></footer>
<div class="abs map" role="img" aria-label="Map of the Dallas–Fort Worth area with the showroom location"></div>
<ul class="abs contact">
  <li><svg viewBox="0 0 22 22"><path d="M5 2l4 4-2.5 2.5c1.5 3 3.5 5 6.5 6.5L15.5 12.5l4 4-3 3C9 19 3 13 2.5 5z" fill="#fff"/></svg>877-555-0142</li>
  <li><svg viewBox="0 0 22 22"><path d="M11 2a6 6 0 0 1 6 6c0 5-6 12-6 12S5 13 5 8a6 6 0 0 1 6-6z" fill="none" stroke="#fff" stroke-width="2"/><circle cx="11" cy="8" r="2" fill="#fff"/></svg>1820 Larkspur Rd, Fort Worth, TX 76140</li>
  <li><svg viewBox="0 0 22 22"><path d="M5 2v17l4-4 3 6 3-1-3-6h6z" fill="#fff"/></svg>Request a quote</li>
  <li><svg viewBox="0 0 22 22"><rect x="2" y="2" width="18" height="18" fill="none" stroke="#fff" stroke-width="2"/><line x1="5" y1="5" x2="17" y2="17" stroke="#fff" stroke-width="2"/></svg>Employment Opportunity</li>
  <li><svg viewBox="0 0 22 22"><rect x="2" y="5" width="18" height="13" fill="none" stroke="#fff" stroke-width="2"/><path d="M2 5l9 7 9-7" fill="none" stroke="#fff" stroke-width="2"/></svg>Email us</li>
</ul>

<div class="abs bottom"><span>Designed by Tidy Themes | Powered by PageForge</span><div class="icons"><i></i><i></i><i></i><i></i></div></div>

</body>
</html>
```